Vornfield Business Cards

Logo files are included. Full "Vornfield" logo should be included on the back of the business card. The H symbol should be included on the front with the contact information.

Vornfield, LLC is the company name and we do commercial construction and real estate development consulting services. Look for a fairly simple card design utilizing our logo.

```html
<!DOCTYPE html>
<html lang="en">
<head>
<meta charset="utf-8">
<title>Vornfield Business Cards</title>
<link href="https://fonts.googleapis.com/css2?family=Libre+Baskerville:wght@700&family=Poppins:wght@400;500;600&display=swap" rel="stylesheet">
<style>
  :root {
    --navy: #132f44;
    --gold: #e6a817;
    --paper: #fbfbf9;
    --stage: #e9e9e7;
    --white: #ffffff;
  }
  * { margin: 0; padding: 0; box-sizing: border-box; }
  html, body { width: 1200px; height: 874px; overflow: hidden; }
  body {
    background: var(--stage);
    font-family: "Poppins", sans-serif;
    position: relative;
  }
  .card {
    position: absolute;
    width: 600px;
    height: 343px;
    border-radius: 18px;
    overflow: hidden;
    box-shadow: 0 10px 28px rgba(0,0,0,0.18);
  }
  /* Back */
  .card-back {
    left: 300px;
    top: 62px;
    background: var(--navy);
    display: flex;
    flex-direction: column;
    align-items: center;
    justify-content: center;
    gap: 22px;
  }
  .back-mark {
    width: 96px;
    height: 96px;
    border-radius: 50%;
    border: 5px solid var(--gold);
  }
  .back-wordmark {
    color: var(--white);
    font-weight: 500;
    font-size: 58px;
    letter-spacing: 3px;
    text-transform: uppercase;
    line-height: 1;
  }
  /* Front */
  .card-front {
    left: 300px;
    top: 468px;
    background: var(--paper);
  }
  .front-wave { position: absolute; inset: 0; }
  .front-logo {
    position: absolute;
    left: 40px;
    top: 40px;
    display: flex;
    align-items: center;
    gap: 14px;
  }
  .front-logo-mark {
    width: 58px;
    height: 58px;
    border-radius: 50%;
    border: 5px solid var(--gold);
  }
  .front-logo-name {
    color: var(--navy);
    font-weight: 600;
    font-size: 30px;
    letter-spacing: 1px;
  }
  .holder {
    position: absolute;
    right: 44px;
    top: 92px;
    text-align: right;
  }
  .holder-name {
    font-family: "Libre Baskerville", serif;
    font-weight: 700;
    font-size: 19px;
    color: var(--navy);
    letter-spacing: 0.5px;
  }
  .holder-title {
    color: var(--gold);
    font-size: 14px;
    margin-top: 2px;
  }
  .contact {
    position: absolute;
    right: 36px;
    top: 206px;
    list-style: none;
    color: var(--white);
    font-size: 12px;
    line-height: 1.3;
  }
  .contact-row {
    display: flex;
    justify-content: flex-end;
    align-items: center;
    gap: 10px;
    text-align: right;
  }
  .contact-row + .contact-row { margin-top: 2px; }
  .contact-icon { width: 12px; height: 12px; flex: none; fill: var(--gold); }
</style>
</head>
<body>

<section class="card card-back" aria-label="Business card back">
  <div class="back-mark"></div>
  <div class="back-wordmark">Vornfield</div>
</section>

<section class="card card-front" aria-label="Business card front">
  <svg class="front-wave" viewBox="0 0 600 343" width="600" height="343">
    <path d="M0,190 C50,290 160,305 260,280 C340,260 370,190 460,178 C525,170 575,182 600,200 L600,343 L0,343 Z" fill="var(--navy)"/>
    <path d="M0,170 C50,282 160,298 255,271" fill="none" stroke="var(--gold)" stroke-width="5"/>
    <path d="M420,172 C490,155 560,162 600,188" fill="none" stroke="var(--navy)" stroke-width="3"/>
  </svg>

  <div class="front-logo">
    <div class="front-logo-mark"></div>
    <div class="front-logo-name">Vornfield</div>
  </div>

  <div class="holder">
    <div class="holder-name">DANIEL HARROW</div>
    <div class="holder-title">President</div>
  </div>

  <ul class="contact">
    <li class="contact-row">
      <span>214 Larkmoor Road<br>Brevik, Oregon 97012</span>
      <svg class="contact-icon" viewBox="0 0 24 24"><path d="M12 2a7 7 0 0 0-7 7c0 5 7 13 7 13s7-8 7-13a7 7 0 0 0-7-7zm0 9.5A2.5 2.5 0 1 1 12 6.5a2.5 2.5 0 0 1 0 5z"/></svg>
    </li>
    <li class="contact-row">
      <span>555-214-7730</span>
      <svg class="contact-icon" viewBox="0 0 24 24"><path d="M6.6 10.8a15 15 0 0 0 6.6 6.6l2.2-2.2a1 1 0 0 1 1-.25 11.4 11.4 0 0 0 3.6.6 1 1 0 0 1 1 1V20a1 1 0 0 1-1 1A17 17 0 0 1 3 4a1 1 0 0 1 1-1h3.5a1 1 0 0 1 1 1c0 1.25.2 2.45.6 3.6a1 1 0 0 1-.25 1z"/></svg>
    </li>
    <li class="contact-row">
      <span>555-618-2094</span>
      <svg class="contact-icon" viewBox="0 0 24 24"><path d="M7 1h10a2 2 0 0 1 2 2v18a2 2 0 0 1-2 2H7a2 2 0 0 1-2-2V3a2 2 0 0 1 2-2zm0 3v14h10V4z"/></svg>
    </li>
    <li class="contact-row">
      <span>555-407-1186</span>
      <svg class="contact-icon" viewBox="0 0 24 24"><path d="M6 2h10v5H6zM3 8h18a1 1 0 0 1 1 1v8h-4v5H6v-5H2V9a1 1 0 0 1 1-1zm5 8v4h8v-4z"/></svg>
    </li>
    <li class="contact-row">
      <span>harrow@vornfield.com</span>
      <svg class="contact-icon" viewBox="0 0 24 24"><path d="M2 5h20v14H2zm2 2v.5l8 5 8-5V7z"/></svg>
    </li>
    <li class="contact-row">
      <span>www.vornfield.com</span>
      <svg class="contact-icon" viewBox="0 0 24 24"><circle cx="12" cy="12" r="10"/></svg>
    </li>
  </ul>
</section>

</body>
</html>
```